MyUptownGroove Web Site Header

Potential designers can visit the site (MyUptownGroove.com) to see our current header. The orange color CANNOT CHANGE! Please do not submit anything different colors. The header needs to contain the following items:
-MyUptownGroove.com
-Do You Sense The Pulse (There IS NO "?" BEHIND THIS!)
- 555.284.6390

I've supplied 13 different photos that you can choose from as a background.

Images of 920 x 150 pixels are the "exact size" that will fit my site. If it's larger, and I have to crop on uploading, I could lose text along the edges. (for what that info is worth!)

Background: Midtown Atlanta is the urban living core of Atlanta. Filled with highrise condominiums, restaurants, shopping and is also called the Heart of the Arts because Wren Playhouse and Calloway Gallery are located there. It's a diverse mixture of people that live there, as well as all the office buildings that are filled daily.

The final design should give a feel of excitement, hence our tagline, Do You Sense The Pulse.
Updates

Project Deadline Extended
Reason: I've gotten some INCREDIBLE designs. It's been hard to make a decision. In fact, may have to select more than one. I'm also in the middle of another project and have been swamped with it.

Target Market(s)

Target market is condo buyers. Age range from 20's to 50's. Heavy concentration of law offices and high-tech companies in the area...so think techy consumer.

Industry/Entity Type

Shopping

Font styles to use
Sans Serif

Colors
f37022

Requirements
Must have
• Phone Number 555.284.6390 or 555-284-6390

MyUptownGroove.com site name in header

```html
<!DOCTYPE html>
<html lang="en">
<head>
<meta charset="utf-8">
<title>MyUptownGroove Web Site Header</title>
<link rel="stylesheet" href="https://fonts.googleapis.com/css2?family=Bebas+Neue&family=Source+Sans+3:wght@400&display=swap">
<style>
  :root {
    --brand-orange: #f37022;
    --band-gold-light: #fcb741;
    --band-gold-deep: #f9a93a;
    --band-white: #ffffff;
    --band-grey: #e4e4e4;
    --frame-white: #ffffff;
    --caption-grey: #b9b9b9;
    --page-bg: #ffffff;
  }
  html, body {
    margin: 0;
    padding: 0;
    width: 1200px;
    height: 748px;
    overflow: hidden;
    background: var(--page-bg);
  }
  .sheet {
    position: relative;
    width: 1200px;
    height: 748px;
  }
  .header-option {
    position: absolute;
    left: 18px;
    width: 1165px;
  }
  .header-option--skyline { top: 16px; }
  .header-option--lounge  { top: 260px; }
  .header-option--pool    { top: 511px; }
  .header-banner {
    display: block;
    width: 1165px;
    height: 190px;
  }
  .banner-text {
    font-family: "Bebas Neue", "Oswald", sans-serif;
  }
  .banner-text--light { fill: var(--band-white); }
  .banner-text--accent { fill: var(--brand-orange); }
  .size-caption {
    margin: 6px 0 0 0;
    font-family: "Source Sans 3", "Myriad Pro", sans-serif;
    font-size: 21px;
    line-height: 1;
    color: var(--caption-grey);
  }
</style>
</head>
<body>
<main class="sheet">

  <svg width="0" height="0" style="position:absolute" aria-hidden="true">
    <defs>
      <linearGradient id="gold-band" x1="0" y1="0" x2="1" y2="0">
        <stop offset="0" stop-color="var(--band-gold-light)"/>
        <stop offset="1" stop-color="var(--band-gold-deep)"/>
      </linearGradient>
      <linearGradient id="white-band" x1="0" y1="0" x2="1" y2="0">
        <stop offset="0" stop-color="var(--band-white)"/>
        <stop offset="1" stop-color="var(--band-grey)"/>
      </linearGradient>
      <linearGradient id="skyline-tones" x1="0" y1="0" x2="0" y2="1">
        <stop offset="0" stop-color="#7fa6d6"/>
        <stop offset="0.45" stop-color="#9bb8d8"/>
        <stop offset="0.75" stop-color="#6f7a86"/>
        <stop offset="1" stop-color="#8a6a58"/>
      </linearGradient>
      <linearGradient id="lounge-tones" x1="0" y1="0" x2="1" y2="1">
        <stop offset="0" stop-color="#9aa7b0"/>
        <stop offset="0.4" stop-color="#7b6a5c"/>
        <stop offset="0.7" stop-color="#b8643a"/>
        <stop offset="1" stop-color="#6b5648"/>
      </linearGradient>
      <linearGradient id="pool-tones" x1="0" y1="0" x2="0" y2="1">
        <stop offset="0" stop-color="#b9cde0"/>
        <stop offset="0.35" stop-color="#5f7f4a"/>
        <stop offset="0.65" stop-color="#7fc6de"/>
        <stop offset="1" stop-color="#a9dcea"/>
      </linearGradient>
      <symbol id="phone-icon" viewBox="0 0 24 24">
        <path fill="currentColor" d="M6.6 10.8c1.4 2.8 3.8 5.1 6.6 6.6l2.2-2.2c.3-.3.7-.4 1-.2 1.1.4 2.3.6 3.6.6.6 0 1 .4 1 1V20c0 .6-.4 1-1 1C10.6 21 3 13.4 3 4c0-.6.4-1 1-1h3.5c.6 0 1 .4 1 1 0 1.3.2 2.5.6 3.6.1.3 0 .7-.2 1z"/>
        <path fill="none" stroke="currentColor" stroke-width="1.8" stroke-linecap="round" d="M14 2.8a7.5 7.5 0 0 1 7.2 7.2M14 6.3a4 4 0 0 1 3.7 3.7"/>
      </symbol>
    </defs>
  </svg>

  <section class="header-option header-option--skyline">
    <svg class="header-banner" viewBox="0 0 1075 175" preserveAspectRatio="none">
      <rect class="band band--gold" x="0" y="0" width="620" height="175" fill="url(#gold-band)"/>
      <rect class="band band--white" x="0" y="57" width="560" height="61" fill="url(#white-band)"/>
      <polygon class="photo-area" role="img" aria-label="Photo of the uptown high-rise skyline under a blue sky"
               points="598,0 1075,0 1075,175 598,175 513,87" fill="url(#skyline-tones)"
               stroke="var(--frame-white)" stroke-width="6" stroke-linejoin="miter"/>
      <text class="banner-text banner-text--light" x="23" y="48" font-size="40" textLength="390" lengthAdjust="spacingAndGlyphs">WWW.MYUPTOWNGROOVE.COM</text>
      <text class="banner-text banner-text--accent" x="23" y="107" font-size="52" textLength="405" lengthAdjust="spacingAndGlyphs">DO YOU SENSE THE PULSE</text>
      <use href="#phone-icon" x="22" y="136" width="30" height="30" color="var(--band-white)"/>
      <text class="banner-text banner-text--light" x="55" y="165" font-size="40">555.284.6390</text>
    </svg>
    <p class="size-caption">920 x 150 pixels</p>
  </section>

  <section class="header-option header-option--lounge">
    <svg class="header-banner" viewBox="0 0 1075 175" preserveAspectRatio="none">
      <rect class="band band--gold" x="0" y="0" width="620" height="175" fill="url(#gold-band)"/>
      <rect class="band band--white" x="0" y="57" width="560" height="61" fill="url(#white-band)"/>
      <polygon class="photo-area" role="img" aria-label="Photo of a rooftop lounge with sofas, orange armchairs and a fireplace"
               points="598,0 1075,0 1075,175 598,175 513,87" fill="url(#lounge-tones)"
               stroke="var(--frame-white)" stroke-width="6" stroke-linejoin="miter"/>
      <text class="banner-text banner-text--light" x="23" y="48" font-size="40" textLength="390" lengthAdjust="spacingAndGlyphs">WWW.MYUPTOWNGROOVE.COM</text>
      <text class="banner-text banner-text--accent" x="23" y="107" font-size="52" textLength="405" lengthAdjust="spacingAndGlyphs">DO YOU SENSE THE PULSE</text>
      <use href="#phone-icon" x="22" y="136" width="30" height="30" color="var(--band-white)"/>
      <text class="banner-text banner-text--light" x="55" y="165" font-size="40">555.284.6390</text>
    </svg>
    <p class="size-caption">920 x 150 pixels</p>
  </section>

  <section class="header-option header-option--pool">
    <svg class="header-banner" viewBox="0 0 1075 175" preserveAspectRatio="none">
      <rect class="band band--gold" x="0" y="0" width="620" height="175" fill="url(#gold-band)"/>
      <rect class="band band--white" x="0" y="57" width="560" height="61" fill="url(#white-band)"/>
      <polygon class="photo-area" role="img" aria-label="Photo of a rooftop pool deck with loungers, planters and trees"
               points="598,0 1075,0 1075,175 598,175 513,87" fill="url(#pool-tones)"
               stroke="var(--frame-white)" stroke-width="6" stroke-linejoin="miter"/>
      <text class="banner-text banner-text--light" x="23" y="48" font-size="40" textLength="390" lengthAdjust="spacingAndGlyphs">WWW.MYUPTOWNGROOVE.COM</text>
      <text class="banner-text banner-text--accent" x="23" y="107" font-size="52" textLength="405" lengthAdjust="spacingAndGlyphs">DO YOU SENSE THE PULSE</text>
      <use href="#phone-icon" x="22" y="136" width="30" height="30" color="var(--band-white)"/>
      <text class="banner-text banner-text--light" x="55" y="165" font-size="40">555.284.6390</text>
    </svg>
    <p class="size-caption">920 x 150 pixels</p>
  </section>

</main>
</body>
</html>
```